Business Card Design

We need a business card for our café and health food store
We are called Mossy Lantern café and Health Foods, so all I have used for a logo so far is a couple of black foot prints under our name.
About 6 foot prints. We are also located by the beach so I thought that maybe some foot prints on the beach which would somehow also represent healthy food and our casual café.
We are open seven days a week and our colour tone is sort of terracotta, sort of Earthy look. We do good coffee and good food for breakfast, lunch and dinner. We are also open seven days for breakfast and lunch, dinner only 3 nights a week.

Industry/Entity Type

Health

Contact Information for Business Card

Mossy Lantern Café and Health Foods
27 Wattlebrook Lane
Apollo Bay
Victoria 3233
Phone 03 5981 4072
ABN 58 276 914 803

```html
<!DOCTYPE html>
<html lang="en">
<head>
<meta charset="utf-8">
<title>Mossy Lantern café and Health Foods – Business Card Options</title>
<link rel="stylesheet" href="https://fonts.googleapis.com/css2?family=Comic+Neue:wght@400;700&display=swap">
<style>
  :root {
    --page: #ffffff;
    --label: #333333;
    --card-centre: #ffffff;
    --card-edge: #dcb272;
    --brown: #6b3f1d;
    --green: #3e7a32;
    --ink: #2b2b2b;
    --shadow: rgba(0, 0, 0, 0.28);
  }
  * { margin: 0; padding: 0; box-sizing: border-box; }
  html, body {
    width: 972px;
    height: 1200px;
    overflow: hidden;
    background: var(--page);
  }
  .sheet {
    position: relative;
    width: 972px;
    height: 1200px;
  }
  .option-number {
    position: absolute;
    font-family: Arial, Helvetica, sans-serif;
    font-size: 28px;
    color: var(--label);
  }
  .option-number--one { left: 76px; top: 116px; }
  .option-number--two { left: 68px; top: 668px; }

  .card {
    position: absolute;
    left: 129px;
    width: 716px;
    height: 423px;
    background: radial-gradient(ellipse 58% 120% at 50% 50%, var(--card-centre) 62%, var(--card-edge) 100%);
    box-shadow: 0 14px 26px -6px var(--shadow);
    font-family: "Comic Neue", sans-serif;
    color: var(--ink);
  }
  .card--one { top: 100px; }
  .card--two { top: 640px; }

  .brand {
    position: absolute;
    left: 63px;
    top: 42px;
    color: var(--brown);
    font-weight: 700;
    line-height: 1;
  }
  .brand__name {
    display: block;
    font-size: 70px;
    letter-spacing: 1px;
  }
  .brand__tagline {
    display: block;
    margin-top: 71px;
    font-size: 32px;
  }
  .card--two .brand__tagline { color: var(--green); }

  .contact {
    position: absolute;
    left: 0;
    top: 252px;
    width: 100%;
    font-size: 22px;
    font-style: normal;
    line-height: 32px;
  }
  .contact__row {
    position: absolute;
    display: flex;
    align-items: center;
    white-space: nowrap;
  }
  .contact__row--street { left: 212px; top: 0; }
  .contact__row--town { left: 241px; top: 32px; }
  .contact__row--phone { left: 264px; top: 72px; font-size: 23px; }
  .contact__row--abn {
    left: 0; width: 100%; top: 114px;
    justify-content: center;
    font-size: 15px;
  }
  .icon { width: 24px; height: 22px; margin-right: 16px; }
  .contact__row--phone .icon { width: 18px; margin-right: 8px; }
  .card--one .icon { fill: var(--brown); }
  .card--two .icon { fill: var(--green); }
</style>
</head>
<body>
<main class="sheet">
  <span class="option-number option-number--one">1</span>
  <section class="card card--one" aria-label="Business card option 1">
    <h1 class="brand">
      <span class="brand__name">Mossy Lantern café</span>
      <span class="brand__tagline">and Health Foods</span>
    </h1>
    <address class="contact">
      <span class="contact__row contact__row--street">
        <svg class="icon" viewBox="0 0 24 22" aria-hidden="true"><path d="M2 7 L12 2 L22 7 Z"/><rect x="3" y="8" width="18" height="12"/><rect x="6" y="11" width="5" height="5" fill="#fff"/><rect x="13" y="11" width="5" height="9" fill="#fff"/></svg>
        27 Wattlebrook Lane
      </span>
      <span class="contact__row contact__row--town">Fernhaven Bay Marlow 4187</span>
      <span class="contact__row contact__row--phone">
        <svg class="icon" viewBox="0 0 18 22" aria-hidden="true"><path d="M4 1 L7 1 L8 6 L6 8 C7 12 9 15 11 16 L13 14 L17 17 L16 20 C9 21 2 12 3 3 Z"/></svg>
        03 5981 4072
      </span>
      <span class="contact__row contact__row--abn">ABN 58 276 914 803</span>
    </address>
  </section>

  <span class="option-number option-number--two">2</span>
  <section class="card card--two" aria-label="Business card option 2">
    <h1 class="brand">
      <span class="brand__name">Mossy Lantern café</span>
      <span class="brand__tagline">and Health Foods</span>
    </h1>
    <address class="contact">
      <span class="contact__row contact__row--street">
        <svg class="icon" viewBox="0 0 24 22" aria-hidden="true"><path d="M2 7 L12 2 L22 7 Z"/><rect x="3" y="8" width="18" height="12"/><rect x="6" y="11" width="5" height="5" fill="#fff"/><rect x="13" y="11" width="5" height="9" fill="#fff"/></svg>
        27 Wattlebrook Lane
      </span>
      <span class="contact__row contact__row--town">Fernhaven Bay Marlow 4187</span>
      <span class="contact__row contact__row--phone">
        <svg class="icon" viewBox="0 0 18 22" aria-hidden="true"><path d="M4 1 L7 1 L8 6 L6 8 C7 12 9 15 11 16 L13 14 L17 17 L16 20 C9 21 2 12 3 3 Z"/></svg>
        03 5981 4072
      </span>
      <span class="contact__row contact__row--abn">ABN 58 276 914 803</span>
    </address>
  </section>
</main>
</body>
</html>
```